Product Information Sheet/Brochure

we are www.belwickharvest.com we grow microgreens for wholesale food service. We are in need of a graphically briliant brochure to offere when marketing. Also, for our new courier box delivery program, we will be sending the micros out with SWIFTOR & KRL in a foam box, this brochure will be with each shipment.

High resolution pictures will be available for the final product/winner. For now please use content from our website.

```html
<!DOCTYPE html>
<html lang="en">
<head>
<meta charset="utf-8">
<title>Belwick Harvest – Microgreens Brochure</title>
<link href="https://fonts.googleapis.com/css2?family=Montserrat:wght@500;600;700;800&family=Open+Sans:wght@400;600;700&family=Lora:ital,wght@0,400;1,400&family=Marcellus&display=swap" rel="stylesheet">
<style>
:root{
  --stage:#2b2b2b;
  --white:#ffffff;
  --forest:#1c7a56;
  --forest-deep:#16694a;
  --leaf:#5ea43c;
  --leaf-deep:#4b8f30;
  --lime:#8dc63f;
  --lime-soft:#a9d45f;
  --ink:#3d3d3d;
  --ink-soft:#555;
}
*{box-sizing:border-box;margin:0;padding:0}
html,body{width:935px;height:1200px;overflow:hidden}
body{background:var(--stage);position:relative;font-family:"Open Sans",Arial,sans-serif;color:var(--ink)}
.abs{position:absolute}
.page{position:absolute;left:131px;width:691px;background:var(--white);overflow:hidden}
.page-front{top:53px;height:537px}
.page-back{top:628px;height:536px}

/* photo placeholders */
.photo{position:absolute}
.photo-basil{left:0;top:0;width:229px;height:124px;background:linear-gradient(135deg,#8cc95a,#4f9a34 60%,#2f6e2a)}
.photo-growroom{left:407px;top:124px;width:284px;height:259px;background:linear-gradient(180deg,#c9cfd0 0%,#9aa39d 35%,#5d8d46 65%,#2f4a2e 100%)}
.photo-sprouts{left:467px;top:454px;width:224px;height:83px;background:linear-gradient(180deg,#ffffff 0%,#d7ebc0 45%,#7fb84c 100%)}
.photo-lab{left:0;top:295px;width:232px;height:161px;background:linear-gradient(135deg,#d9e4d6,#7fb060 45%,#c9632c 75%,#5c8a45)}
.photo-shoots{left:241px;top:367px;width:210px;height:89px;background:linear-gradient(180deg,#ffffff 0%,#dcedc6 40%,#86bd50 100%)}

/* front: title block */
.title-fresh{left:258px;top:30px;font-family:"Marcellus",Georgia,serif;font-size:70px;line-height:1;color:var(--lime)}
.title-cut{left:302px;top:18px;font-family:"Lora",Georgia,serif;font-style:italic;font-size:26px;line-height:1;color:var(--lime)}
.title-sub{left:253px;top:99px;font-family:"Lora",Georgia,serif;font-style:italic;font-size:13px;line-height:16px;color:var(--ink);white-space:nowrap}
.truck{left:398px;top:96px;width:34px;height:23px}

/* brand */
.brand-dot{left:567px;top:18px;width:50px;height:50px;border-radius:50%;background:var(--lime)}
.brand-name{left:477px;top:78px;width:214px;text-align:center;font-family:"Montserrat",Arial,sans-serif;font-weight:700;font-size:21px;color:var(--forest-deep)}
.brand-tag{left:477px;top:106px;width:214px;text-align:center;font-family:"Open Sans",Arial,sans-serif;font-style:italic;font-weight:600;font-size:11.5px;color:var(--leaf)}

/* features */
.feature{position:absolute;left:0;width:229px}
.feature-icon{position:absolute;left:16px;width:38px;height:38px}
.feature h3{position:absolute;left:59px;top:0;font-family:"Montserrat",Arial,sans-serif;font-weight:700;font-size:12px;color:var(--lime);letter-spacing:.2px}
.feature p{position:absolute;left:59px;top:15px;width:165px;font-size:9.4px;line-height:11.3px;color:var(--ink-soft)}

/* contact */
.contact{left:229px;top:124px;width:178px;height:259px;background:var(--forest)}
.contact-head{position:absolute;left:22px;top:17px;width:140px;height:26px;border:1.5px solid var(--white);color:var(--white);font-family:"Montserrat",Arial,sans-serif;font-weight:700;font-size:13px;text-align:center;line-height:23px;letter-spacing:.5px}
.contact-icon{position:absolute;left:79px;width:20px;height:20px}
.contact-line{position:absolute;left:0;width:178px;text-align:center;color:var(--white);font-size:10.5px;line-height:13px}
.contact-web{font-family:"Montserrat",Arial,sans-serif;font-weight:700;font-size:14px}

/* lime band */
.band{left:229px;top:383px;width:462px;height:71px;background:var(--lime)}
.hours{position:absolute;left:0;top:10px;width:238px;text-align:center;color:var(--white);font-size:10.5px;line-height:13px}
.partners-title{position:absolute;left:0;top:47px;width:238px;text-align:center;color:var(--white);font-family:"Montserrat",Arial,sans-serif;font-weight:700;font-size:14px;letter-spacing:.6px}
.cta-small{position:absolute;left:238px;top:18px;width:224px;text-align:center;color:var(--white);font-family:"Montserrat",Arial,sans-serif;font-weight:700;font-size:13px;letter-spacing:.4px}
.cta-big{position:absolute;left:238px;top:32px;width:224px;text-align:center;color:var(--white);font-family:"Montserrat",Arial,sans-serif;font-weight:800;font-size:30px;letter-spacing:1px;line-height:1.1}

.partner{position:absolute;border-radius:50%}

/* back: mission */
.mission{left:0;top:0;width:458px;height:82px;background:var(--leaf)}
.mission-label{position:absolute;left:0;top:0;width:100px;height:82px;background:var(--leaf-deep);color:var(--white);font-family:"Montserrat",Arial,sans-serif;font-weight:700;font-size:14.5px;line-height:16px;text-align:center;padding-top:25px;letter-spacing:.5px}
.mission-text{position:absolute;left:110px;top:16px;width:338px;color:var(--white);font-size:9.5px;line-height:11.5px;text-align:justify}

.section-title{position:absolute;font-family:"Montserrat",Arial,sans-serif;font-weight:700;font-size:24px;text-align:center}
.about-title{left:0;top:104px;width:250px;color:var(--forest-deep)}
.about-text{left:17px;top:144px;width:205px;font-size:9.3px;line-height:11.1px;text-align:justify;color:var(--ink)}
.greens-title{left:240px;top:104px;width:215px;color:var(--lime)}
.facts{left:246px;top:144px;width:208px;list-style:none}
.facts li{position:relative;padding-left:9px;font-size:9.5px;line-height:11.4px;color:var(--ink);margin-bottom:10px}
.facts li::before{content:"";position:absolute;left:0;top:4px;width:4px;height:4px;border-radius:50%;background:var(--leaf)}

/* varieties */
.varieties{left:458px;top:0;width:233px;height:458px;background:var(--forest)}
.variety{position:absolute;width:66px;height:66px;border-radius:50%;background:var(--white);border:4px solid #e3efe8;box-shadow:0 2px 4px rgba(0,0,0,.25)}
.variety-photo{position:absolute;left:10px;top:10px;width:38px;height:38px;border-radius:50%}
.variety-name{position:absolute;width:90px;text-align:center;color:#e6f2ea;font-size:7.8px;letter-spacing:.3px;text-transform:uppercase;white-space:nowrap}

/* closing band */
.closing{left:0;top:458px;width:691px;height:78px;background:linear-gradient(90deg,var(--forest) 0%,var(--forest) 30%,#5ea75a 50%,var(--lime) 75%,var(--lime-soft) 100%)}
.closing-note{position:absolute;left:17px;top:6px;width:210px;color:var(--white);font-size:9.6px;line-height:11.5px}
.closing-line{position:absolute;left:300px;top:13px;width:340px;text-align:center;color:var(--white);font-family:"Lora",Georgia,serif;font-size:20px;line-height:24px}
</style>
</head>
<body>

<!-- FRONT -->
<section class="page page-front">
  <div class="photo photo-basil" role="img" aria-label="Close-up of fresh basil microgreens in a growing tray"></div>

  <div class="abs title-fresh">Fresh</div>
  <div class="abs title-cut">Cut</div>
  <div class="abs title-sub">Delivered to your door!</div>
  <svg class="abs truck" viewBox="0 0 36 24" aria-hidden="true">
    <rect x="1" y="4" width="20" height="13" rx="1" fill="#8dc63f"/>
    <path d="M22 8h7l5 5v4H22z" fill="#8dc63f"/>
    <circle cx="8" cy="19" r="3" fill="#3d3d3d"/><circle cx="28" cy="19" r="3" fill="#3d3d3d"/>
  </svg>

  <div class="abs brand-dot"></div>
  <div class="abs brand-name">Belwick Harvest</div>
  <div class="abs brand-tag">“Where good things grow”</div>

  <div class="feature" style="top:154px">
    <svg class="feature-icon" style="top:2px" viewBox="0 0 38 38" aria-hidden="true"><path d="M4 32C6 14 18 6 34 6c0 16-10 26-26 24z" fill="#5ea43c"/><path d="M4 34L24 14" stroke="#fff" stroke-width="2"/></svg>
    <h3>GROWING</h3>
    <p>Belwick Harvest grows all crops indoors with artificial light and climate control, we use our proprietary growing technology to deliver crops not affected by weather.</p>
  </div>
  <div class="feature" style="top:261px">
    <svg class="feature-icon" style="top:6px" viewBox="0 0 38 38" aria-hidden="true"><circle cx="19" cy="19" r="16" fill="none" stroke="#5ea43c" stroke-width="3"/><path d="M11 19l6 6 11-12" fill="none" stroke="#5ea43c" stroke-width="3.5" stroke-linecap="round" stroke-linejoin="round"/></svg>
    <h3>ENVIRONMENT</h3>
    <p>Since Belwick Harvest grows 100% indoors and we: Use a fraction of the water used in conventional growing methods Have no need for pesticides or herbicides</p>
  </div>
  <div class="feature" style="top:355px">
    <svg class="feature-icon" style="top:12px" viewBox="0 0 38 38" aria-hidden="true"><g fill="none" stroke="#5ea43c" stroke-width="3"><path d="M2 8q4-4 8 0t8 0 8 0 8 0"/><path d="M2 18q4-4 8 0t8 0 8 0 8 0"/><path d="M2 28q4-4 8 0t8 0 8 0 8 0"/></g></svg>
    <h3>PRODUCT</h3>
    <p>Belwick Harvest products have better color, better flavor and last longer on the shelf than competing products, that means better quality product and lower food costs for our customers!</p>
  </div>
  <div class="feature" style="top:461px">
    <svg class="feature-icon" style="top:6px" viewBox="0 0 38 38" aria-hidden="true"><path d="M19 2l8 11h-4l7 9h-5l7 9H6l7-9H8l7-9h-4z" fill="#5ea43c"/><rect x="17" y="31" width="4" height="6" fill="#5ea43c"/></svg>
    <h3>FOOD SAFETY</h3>
    <p>Belwick Harvest is a USDA GAP/GHP certified grower, we have maintained our certification since 2016.</p>
  </div>

  <div class="abs contact">
    <div class="contact-head">CONTACT US</div>
    <svg class="contact-icon" style="top:59px" viewBox="0 0 20 20" aria-hidden="true"><circle cx="10" cy="10" r="10" fill="#8dc63f"/><path d="M7 5l2 2-1 2q1 2 3 3l2-1 2 2-1 2q-5 0-8-4-2-3-1-5z" fill="#fff"/></svg>
    <div class="contact-line" style="top:82px">713 555 0148</div>
    <svg class="contact-icon" style="top:101px" viewBox="0 0 20 20" aria-hidden="true"><circle cx="10" cy="10" r="10" fill="#8dc63f"/><rect x="5" y="6.5" width="10" height="7" fill="none" stroke="#fff" stroke-width="1.3"/><path d="M5 7l5 4 5-4" fill="none" stroke="#fff" stroke-width="1.3"/></svg>
    <div class="contact-line" style="top:123px">info@belwickharvest.com</div>
    <svg class="contact-icon" style="top:142px" viewBox="0 0 20 20" aria-hidden="true"><circle cx="10" cy="10" r="10" fill="#8dc63f"/><path d="M10 16s-4-4.5-4-7.5a4 4 0 018 0c0 3-4 7.5-4 7.5z" fill="#fff"/><circle cx="10" cy="8.5" r="1.5" fill="#8dc63f"/></svg>
    <div class="contact-line" style="top:164px">4180 Orchard Lane<br>Millbrook TX 77400</div>
    <svg class="contact-icon" style="top:196px" viewBox="0 0 20 20" aria-hidden="true"><circle cx="10" cy="10" r="10" fill="#8dc63f"/><g fill="none" stroke="#fff" stroke-width="1.1"><circle cx="10" cy="10" r="5.5"/><ellipse cx="10" cy="10" rx="2.3" ry="5.5"/><path d="M4.5 10h11"/></g></svg>
    <div class="contact-line contact-web" style="top:219px">belwickharvest.com</div>
  </div>

  <div class="photo photo-growroom" role="img" aria-label="Indoor grow room with trays of microgreens under LED light bars"></div>

  <div class="abs band">
    <div class="hours">Monday To Friday 8am – 5pm<br>Weekend: By Appoinment</div>
    <div class="partners-title">WHOLESALE PARTNERS</div>
    <div class="cta-small">INCREASE YOUR CULINARY</div>
    <div class="cta-big">EXPERIENCE</div>
  </div>

  <div class="partner" style="left:282px;top:465px;width:36px;height:22px;border-radius:3px;background:#c5313a"></div>
  <div class="partner" style="left:325px;top:465px;width:52px;height:22px;background:#1b1b1b"></div>
  <div class="partner" style="left:384px;top:463px;width:30px;height:26px;border-radius:4px;background:#2d4f9e"></div>
  <div class="partner" style="left:240px;top:491px;width:30px;height:30px;background:#d93a2a"></div>
  <div class="partner" style="left:276px;top:492px;width:31px;height:30px;background:#1b1b1b"></div>
  <div class="partner" style="left:316px;top:494px;width:56px;height:24px;border-radius:4px;background:#d8262d"></div>
  <div class="partner" style="left:378px;top:500px;width:70px;height:12px;border-radius:2px;background:#e0a0a6"></div>

  <div class="photo photo-sprouts" role="img" aria-label="Sunflower microgreen shoots"></div>
</section>

<!-- BACK -->
<section class="page page-back">
  <div class="abs mission">
    <div class="mission-label">OUR<br>MISSION</div>
    <p class="mission-text">to provide superior &amp; nutrient-rich microgreen products at affordable prices to independent consumers in the Gulf Coast region of the United States who appreciate quality, flavor and freshness. And to leverage our geographic advantage as it applies to getting the best microgreens available today from farm to your table as soon as possible.</p>
  </div>

  <h2 class="section-title about-title">About Us</h2>
  <p class="abs about-text">Belwick Harvest has supplied high quality microgreens to the Houston area since early 2015, currently Belwick Harvest micros are incorporated into approximately 268,000 plates a week in the Houston and Dallas Area! Belwick Harvest has a solid track record in supplying microgreens and microgreen mixes that meet the highest standards (and most discerning tastes) of leading area restaurants, we are also known for our traditional non-GMO and herbicide/pesticide free microgreen products.</p>
  <div class="photo photo-lab" role="img" aria-label="Two growers in lab coats inspecting shelves of greens in an indoor farm"></div>

  <h2 class="section-title greens-title">Microgreens</h2>
  <ul class="abs facts">
    <li>Microgreens are very small edible plants produced from vegetable and herb seeds.</li>
    <li>Microgreens are harvested while they are still very small plants, they range in size from 1 to 2 inches long, including the stem and leaves.</li>
    <li>Microgreens have surprisingly intense flavors considering their small size, their flavors vary from sweet to spicy and their texture can range from melt in your mouth to crunchy.</li>
    <li>Microgreens are very nutritious, they are said to contain from 4 – 40 times more vitamins and minerals ounce per ounce than their mature plant cousins</li>
  </ul>
  <div class="photo photo-shoots" role="img" aria-label="Sunflower microgreen shoots growing in soil"></div>

  <div class="abs varieties">
    <div class="variety" style="left:12px;top:24px"><div class="variety-photo" style="background:#7fa95a" role="img" aria-label="Wasabi microgreens"></div></div>
    <div class="variety-name" style="left:0;top:96px">Wasabi</div>
    <div class="variety" style="left:85px;top:24px;background:var(--lime)">
      <svg class="abs" style="left:14px;top:-14px;width:30px;height:22px" viewBox="0 0 30 22" aria-hidden="true"><path d="M2 20C4 8 14 2 28 2c0 12-10 19-24 18z" fill="#8dc63f"/></svg>
      <div class="abs" style="left:0;top:16px;width:58px;text-align:center;color:#fff;font-family:'Montserrat',Arial,sans-serif;font-weight:800;font-size:12px">100%</div>
      <div class="abs" style="left:0;top:31px;width:58px;text-align:center;color:#fff;font-size:8px">NON GMO</div>
    </div>
    <div class="variety" style="left:155px;top:24px"><div class="variety-photo" style="background:#5e6b3a" role="img" aria-label="Red veined sorrel microgreens"></div></div>
    <div class="variety-name" style="left:143px;top:96px">Red Veined Sorrel</div>

    <div class="variety" style="left:12px;top:108px"><div class="variety-photo" style="background:#6b4a3e" role="img" aria-label="Red mustard microgreens"></div></div>
    <div class="variety-name" style="left:0;top:180px">Red Mustard</div>
    <div class="variety" style="left:85px;top:108px"><div class="variety-photo" style="background:#b9d79a" role="img" aria-label="Pea tendril microgreens"></div></div>
    <div class="variety-name" style="left:73px;top:180px">Pea Tendril</div>
    <div class="variety" style="left:155px;top:108px"><div class="variety-photo" style="background:#d8d65a" role="img" aria-label="Corn shoot microgreens"></div></div>
    <div class="variety-name" style="left:143px;top:180px">Corn Shoots</div>

    <div class="variety" style="left:12px;top:194px"><div class="variety-photo" style="background:#5a4a3a" role="img" aria-label="Asian mix microgreens"></div></div>
    <div class="variety-name" style="left:0;top:267px">Asian Mix</div>
    <div class="variety" style="left:85px;top:194px"><div class="variety-photo" style="background:#4f9a3a" role="img" aria-label="Pea shoot microgreens"></div></div>
    <div class="variety-name" style="left:73px;top:265px">Pea Shoots</div>
    <div class="variety" style="left:155px;top:194px"><div class="variety-photo" style="background:#3e7a30" role="img" aria-label="Basil microgreens"></div></div>
    <div class="variety-name" style="left:143px;top:267px">Basil</div>

    <div class="variety" style="left:12px;top:281px"><div class="variety-photo" style="background:#6e6a44" role="img" aria-label="Rainbow mix microgreens"></div></div>
    <div class="variety-name" style="left:0;top:354px">Rainbow Mix</div>
    <div class="variety" style="left:85px;top:281px"><div class="variety-photo" style="background:#5f9b3c" role="img" aria-label="Arugula microgreens"></div></div>
    <div class="variety-name" style="left:73px;top:352px">Arugula</div>
    <div class="variety" style="left:155px;top:281px"><div class="variety-photo" style="background:#6b4870" role="img" aria-label="Purple radish microgreens"></div></div>
    <div class="variety-name" style="left:143px;top:354px">Purple Radish</div>

    <div class="variety" style="left:12px;top:369px"><div class="variety-photo" style="background:#8fb56e" role="img" aria-label="Chervil microgreens"></div></div>
    <div class="variety-name" style="left:0;top:441px">Chervil</div>
    <div class="variety" style="left:85px;top:369px"><div class="variety-photo" style="background:#9a2f4a" role="img" aria-label="Bulls blood microgreens"></div></div>
    <div class="variety-name" style="left:73px;top:441px">Bulls Blood</div>
    <div class="variety" style="left:155px;top:369px"><div class="variety-photo" style="background:#4e8f35" role="img" aria-label="Cilantro microgreens"></div></div>
    <div class="variety-name" style="left:143px;top:441px">Cilantro</div>
  </div>

  <div class="abs closing">
    <p class="closing-note">Our customers are restaurants, home chefs, catering companies, private chefs and cooking enthusiasts looking to add a new dimension of flavor and freshness to their culinary creations.</p>
    <p class="closing-line">We look forward to increasing<br>your culinary experience!</p>
  </div>
</section>

</body>
</html>
```